Dynamic Website Design For Dynamic Speaker and Business Coach!

Professional Website Design for a for a Professional Business coach, Business trainer, and Speaker.

Note: This is for design only. No coding required. We want to see your ideas for a great website! This will be a FUN design and not boring like others you may work on.

Please let your creative ideas flow. We have given you a ton of info along with videos to help you understand what we are after, however we WANT your creativity to shine through in your designs!

We are a professional company that has run hundreds of crowdsourced projects on multiple platforms. If you participate in this contest (we hope you do) you can expect great video feedback, consistent feedback, and also our guarantee that if we know your website design will not be what we are looking for we will notify you so you don’t waste your time if there is no chance of you winning.

We respect and recognize this is how you make your living and we will not play games. We look forward to an awesome contest and awesome website designs.

Design Brief:

We are looking for a fresh and fun new design for

http://www.brightpath-advisory.net

This individual (Dana Holloway) teaches and trains corporations and businesses in the fields of leadership, sales, communication, business operations etc. Additionally this business teaches and mentors business professionals in a small group level or 1 on 1.

The website needs to convey trust, professionalism, and affluent, while at the same time having some personality!

This business operates on 3 core principles that we would like to see incorporated into the logo if it is a good fit. The 3 principals are:

Focus
Accountability
Results

Here is a video to help explain what we like about the current site and what we don’t like:
http://clipvault.example/t/QwpLmr82kTnb

As you can see the website is geared towards business professionals. Please look over the website to learn what they do. Obviously this is not a good website so we need your help.

We want a website that is professional-looking, has personality and is geared more towards promoting Dana Holloway, the owner of Summit Path Advisory as a Speaker and Business Consultant. The more you can incorporate clean, professional and fun personality elements into the design, the better off you are at winning.

Here are some examples of other sites in their business that have some things we like:

http://velvetcompass.com Please watch video to learn what we like and don’t like:
http://clipvault.example/t/NrtHq7YpLwc

http://tallpinegrowth.com Please watch video to learn what we like and don’t like:
http://clipvault.example/t/J8vDkrWa

http://www.marthaquince.com Please watch video to learn what we like and don’t like:
http://clipvault.example/t/Pz3mx9Rb2Kq

http://www.vantix7.com Please watch video to learn what we like and don’t like:
http://clipvault.example/t/7Gwe4sNhydv

NOTE: We do not want to copy anything outright. We want to learn, model and take their ideas and make them better. We also want to be flexible and take what we like along with your creativity to make an amazing design.

Here is what we are looking for in more specific terms:

Colors: We like the darker blue (not the light blue like the site) and also a burnt orange. I’ve attached her Logo so you can get an idea and feel for the colors.

When looking at colors please know that the current site and look is NOT what we are going for. We are going for a clean and professional look but also a look that is BOLD, FUN, and Vibrant (hence the colors).

Menu: Horizontal. We like bold and easy to read menu items. Don’t make it small and cluttered.

Site Structure: Clean and easy to navigate. We have a lot of content to display so we need a clean structure that breaks up the text and content areas.
Images: Please pull images from the current site. We can always replace the images of course, but if you show them “their own stuff” in the new design you will be closer to winning because it will feel more like “them”

Look and Feel: Professional. Fun. High-End. Business-like. This website needs to convey that Dana Holloway and Summit Path Advisory are professional. That Dana Holloway is a sought-after Speaker and Business Consultant who knows what she is talking about; can be serious when she needs to be, but also likes to have fun with her clients. This site must convey that!

Content Areas: It is a safe bet that if it is on the current site we need it on the new site. So don’t drop anything as it makes it hard to “cut content”.

What we don't want: We do not want clutter, boring, or templates or themes. We don’t want too cartoony, too cute, or too fancy… Be creative!

Out of respect to professional designers who really are working hard to win if you do not follow this brief, you submit worn out themes, templates, or boring designs you will be eliminated. We are offering great prize money for this so we expect great visual designs.
Updates

Project Deadline Extended
Reason: Our client is out of town, and waiting to hear feedback from them. So, in the meantime, we wanted to keep the project going to see what else you designers can come up with. As soon as we hear back from our client, we will pass along the info. Thanks!

Target Market(s)

Target Audience is entrepreneurs and business professionals alike. This is all business to business stuff.

This person teaches and trains startups and billion dollar companies. The common thread is that they are all businesses and companies who need help in various areas including sales, communication, business operations, etc.

Industry/Entity Type

Business

Font styles to use
Sans Serif

Requirements
Must have
• Brief is very detailed. Please review
Nice to have
Should not have

```html
<!DOCTYPE html>
<html lang="en">
<head>
<meta charset="utf-8">
<title>Summit Path Advisory — Albuquerque Business Coaching and Consulting</title>
<link rel="stylesheet" href="https://fonts.googleapis.com/css2?family=Quicksand:wght@400;500;700&family=Open+Sans:ital,wght@0,400;0,600;0,700;1,400;1,700&display=swap">
<style>
:root{
  --navy:#0d3a66;
  --navy-deep:#082a4d;
  --orange:#ec6a1a;
  --orange-soft:#f08a3c;
  --ink:#222;
  --text:#333;
  --muted:#666;
  --paper:#fff;
  --mist:#f1f1f1;
  --charcoal:#1f1f1f;
  --charcoal-2:#2b2b2b;
  --steel:#3c4350;
  --line:#4a90d9;
}
*{box-sizing:border-box;margin:0;padding:0}
html,body{width:1200px;height:3048px;overflow:hidden}
body{font-family:"Open Sans",Arial,sans-serif;color:var(--text);background:var(--paper);position:relative}
section,header,footer,nav{position:absolute;left:0;width:1200px}

/* header */
.masthead{top:0;height:140px;background:#f7f7f7;display:flex;align-items:center;justify-content:center;gap:16px}
.brand-dot{width:46px;height:46px;border-radius:50%;background:var(--orange)}
.brand-name{font-family:"Quicksand",sans-serif;font-weight:700;font-size:36px;color:var(--navy)}

.main-nav{top:140px;height:43px;background:var(--navy-deep);display:flex;align-items:center;justify-content:space-between;padding:0 22px}
.main-nav a{color:#fff;text-decoration:none;font-size:14px;font-weight:600;letter-spacing:.3px;text-transform:uppercase}

/* hero */
.hero{top:183px;height:389px;background:linear-gradient(100deg,#0b3561 0%,#124679 45%,#0e3b69 100%);color:#fff}
.hero-backdrop{position:absolute;left:80px;top:40px;width:560px;height:250px;background:linear-gradient(90deg,rgba(255,255,255,.05),rgba(255,255,255,.12),rgba(255,255,255,.03))}
.hero-title{position:absolute;left:40px;width:640px;top:38px;text-align:center;font-family:"Quicksand",sans-serif;font-size:30px;line-height:38px;font-weight:500;text-transform:uppercase;letter-spacing:.5px;white-space:nowrap}
.hero-sub{position:absolute;left:80px;width:560px;top:126px;text-align:center;font-family:"Quicksand",sans-serif;font-size:20px;line-height:26px}
.play{position:absolute;left:312px;top:180px}
.hero-btn{position:absolute;top:312px;height:46px;border-radius:4px;display:flex;align-items:center;gap:12px;padding-left:20px;font-size:14px;font-weight:600;text-transform:uppercase;color:#fff}
.hero-btn .ring{width:20px;height:20px;border:2px solid #fff;border-radius:50%;display:flex;align-items:center;justify-content:center;font-size:15px;line-height:1}
.btn-blue{left:173px;width:279px;background:#2c7fd1}
.btn-orange{left:473px;width:234px;background:var(--orange)}
.portrait{position:absolute;border-radius:50%;border:6px solid rgba(255,255,255,.75)}
.hero-portrait{left:830px;top:33px;width:330px;height:330px;background:radial-gradient(circle at 50% 40%,#b07a5a 0%,#6b3a24 45%,#2a2a2a 100%)}

/* intro */
.intro{top:572px;height:267px;padding:0 64px}
.section-title{font-family:"Quicksand",sans-serif;font-size:31px;font-weight:500;color:var(--ink);text-align:center;text-transform:uppercase}
.accent{color:var(--orange)}
.intro .section-title{margin-top:26px;display:flex;justify-content:center;align-items:center;gap:12px}
.plus-ring{width:24px;height:24px;border:2px solid var(--orange);border-radius:50%;color:var(--orange);display:inline-flex;align-items:center;justify-content:center;font-size:18px;line-height:1}
.intro p{font-size:17px;line-height:24px;margin-top:12px}
.intro p:first-of-type{margin-top:32px}

/* shared list + box */
.band-grey{background:var(--mist)}
.points{position:absolute;left:64px;list-style:none}
.points li{display:flex;align-items:center;gap:16px;font-size:17px;color:var(--ink)}
.points li::before{content:"";width:40px;height:2px;background:var(--line);flex:none}
.callout{position:absolute;border:2px solid var(--orange);border-radius:22px;background:#fff;padding:28px 26px;font-size:17px;line-height:24px;color:var(--ink);font-weight:600}
.callout .plus-ring{position:absolute;left:-2px;top:-2px;width:22px;height:22px;font-size:16px;background:#fff}

.coach{top:839px;height:356px}
.coach-title{position:absolute;top:32px;width:100%;text-align:center;font-family:"Quicksand",sans-serif;font-size:35px;font-weight:500;color:var(--ink)}
.coach-title span{display:block;color:var(--orange);text-transform:uppercase;font-size:31px;margin-top:6px}
.rule{position:absolute;left:540px;width:120px;height:4px;background:var(--orange)}
.coach .points{top:168px}
.coach .points li{height:34px}
.coach .callout{left:813px;top:140px;width:344px;min-height:178px;padding:26px 24px;font-size:16.5px;line-height:23px}

.expect{top:1195px;height:127px;text-align:center;font-family:"Quicksand",sans-serif;font-size:27px;color:var(--ink);padding-top:40px;line-height:34px}
.expect .accent{text-transform:uppercase}

.duo{top:1322px;height:158px;display:flex}
.duo div{height:158px;color:#fff;font-size:17px;line-height:24px;padding:28px 30px}
.duo .navy{width:623px;background:var(--navy)}
.duo .orange{width:577px;background:var(--orange)}

.promise{top:1480px;height:388px}
.promise-title{position:absolute;top:66px;width:100%;text-align:center;font-family:"Quicksand",sans-serif;font-size:26px;font-weight:500;color:var(--ink);line-height:34px}
.promise-title .accent{text-transform:uppercase}
.promise .points{top:170px}
.promise .points li{height:30px;font-size:16.5px}
.promise .callout{left:788px;top:146px;width:394px;min-height:180px;font-weight:400;font-size:15.5px;line-height:21px;padding:22px 20px}

/* feature */
.feature{top:1868px;height:471px;background:radial-gradient(ellipse at 60% 45%,#5a6372 0%,#3a404c 45%,#20242b 100%);color:#fff}
.feature-portrait{left:145px;top:95px;width:294px;height:294px;background:radial-gradient(circle at 50% 40%,#b07a5a 0%,#6b3a24 45%,#2a2a2a 100%)}
.feature-kicker{position:absolute;left:521px;top:140px;font-family:"Quicksand",sans-serif;font-size:50px;font-weight:500}
.feature-name{position:absolute;left:521px;top:200px;font-family:"Quicksand",sans-serif;font-size:74px;font-weight:500;text-transform:uppercase;letter-spacing:1px;white-space:nowrap}
.know-more{position:absolute;left:534px;top:300px;width:234px;height:71px;border:2px solid rgba(255,255,255,.55);border-radius:6px;background:rgba(255,255,255,.08);display:flex;align-items:center;justify-content:center;gap:14px;font-size:18px;font-weight:600;text-transform:uppercase}

/* testimonial */
.voices{top:2339px;height:343px;text-align:center}
.voices svg{margin-top:24px}
.voices h2{font-family:"Quicksand",sans-serif;font-size:40px;font-weight:500;color:var(--ink);margin-top:2px}
.voices h2 em{font-style:italic;font-weight:400}
.voices blockquote{width:1060px;margin:18px auto 0;font-size:16.5px;line-height:23px;color:var(--ink)}
.voices cite{display:flex;justify-content:center;align-items:center;gap:14px;margin-top:20px;font-weight:700;font-size:17px;color:var(--ink)}
.voices cite::before{content:"";width:40px;height:2px;background:var(--ink)}

/* footer */
.contact{top:2682px;height:292px;background:var(--charcoal);color:#bbb}
.signup{position:absolute;left:25px;top:60px;width:230px;text-align:right;font-size:15px;line-height:22px;color:#ddd}
.signup strong{font-size:21px;color:#fff}
.field{position:absolute;border-bottom:1px solid #555;font-size:14px;color:#777;padding-bottom:6px}
.field-name{left:300px;top:40px;width:210px}
.field-email{left:300px;top:105px;width:210px}
.field-msg{left:585px;top:40px;width:240px;height:80px;border:none}
.field-msg .box{position:absolute;left:0;top:24px;width:240px;height:60px;border:1px solid #555}
.send{position:absolute;left:295px;top:170px;width:531px;height:46px;background:#111;color:#ddd;font-size:14px;font-weight:600;display:flex;align-items:center;justify-content:center;letter-spacing:1px}
.reach{position:absolute;left:890px;top:40px;list-style:none}
.reach li{display:flex;gap:26px;margin-bottom:22px;align-items:flex-start}
.reach .label{font-size:13px;text-transform:uppercase;color:#999;letter-spacing:.5px}
.reach .value{font-size:14px;color:#ccc;line-height:19px;width:240px}

.legal{top:2974px;height:74px;background:var(--charcoal-2);text-align:center;color:#aaa;font-size:13px;padding-top:14px;text-transform:uppercase}
.social{display:flex;justify-content:center;gap:14px;margin-top:14px}
.social span{width:24px;height:24px;border-radius:50%;background:#3a3a3a;border:1px solid #555}
</style>
</head>
<body>

<header class="masthead">
  <span class="brand-dot"></span>
  <span class="brand-name">Summit Path Advisory</span>
</header>

<nav class="main-nav">
  <a>Home</a><a>Passion</a><a>Who We Are</a><a>Speaker</a><a>Free Videos</a><a>Web TV Show</a><a>Testimonials</a><a>Harbor Learning</a><a>Blog</a><a>Contact</a>
</nav>

<section class="hero">
  <div class="hero-backdrop" role="img" aria-label="Faded presentation slide backdrop behind the headline"></div>
  <h1 class="hero-title">Albuquerque<br>Business Coaching and Consulting</h1>
  <p class="hero-sub">Check out our video presentation</p>
  <svg class="play" width="96" height="104" viewBox="0 0 96 104">
    <polygon points="48,4 92,28 92,76 48,100 4,76 4,28" fill="none" stroke="#fff" stroke-width="4"/>
    <polygon points="38,34 66,52 38,70" fill="#fff"/>
  </svg>
  <div class="hero-btn btn-blue"><span class="ring">+</span>Unplugged Web TV Show</div>
  <div class="hero-btn btn-orange"><span class="ring">+</span>Free Insider Videos</div>
  <div class="portrait hero-portrait" role="img" aria-label="Portrait photo of Dana Holloway"></div>
</section>

<section class="intro">
  <h2 class="section-title"><span class="plus-ring">+</span><span>Change your thinking, <span class="accent">change your results!</span></span></h2>
  <p>Are you searching to bridge the gap between where you are and where you want to be?</p>
  <p>As you face greater pressure to "move the needle" on your company's productivity and bottom line profitability, how prepared are you to step in and shine as the leader?</p>
  <p>We specialize in guiding leaders to become easier to follow.&nbsp; You're in the Right Place.</p>
</section>

<section class="coach band-grey">
  <h2 class="coach-title">Albuquerque Business Coach:<span>Focus, Accountability, &amp; Results</span></h2>
  <div class="rule" style="top:135px"></div>
  <ul class="points">
    <li>Development Of An Operational Plan That Links All Departments</li>
    <li>Implementation And Monitoring Individual And Departmental Plans</li>
    <li>Diagnosing Employee Training Needs</li>
    <li>Delivering The Training To Develop Leaders And Staff</li>
    <li>Coach Leaders, Individuals And Teams</li>
  </ul>
  <div class="callout"><span class="plus-ring">+</span>Whether you're leading a company, or are an employee, all of us have a role to play in contributing to the profit and the future of the company.</div>
</section>

<section class="expect">
  <p>Your organization expects you to<br><span class="accent">Deliver value by delivering results.</span></p>
</section>

<section class="duo">
  <div class="navy">At Summit Path Advisory, we know as a company or as individuals, clarity of the direction captured in an annual plan that is monitored monthly is one of the surest, quickest and most profitable ways of getting ahead in these challenging times.</div>
  <div class="orange">What is the missing link in your business?&nbsp; What are you searching for?&nbsp; Email me today, conversation is complimentary to investigate where we start building the business you envision for tomorrow.</div>
</section>

<section class="promise band-grey">
  <h2 class="promise-title"><span class="accent">Summit Path Advisory has delivered on our promise.</span><br>Our clients learn to:</h2>
  <ul class="points">
    <li>Establish new patterns of productivity for the business</li>
    <li>Clarification of future goals, targets and benchmarks</li>
    <li>Implement actionable steps around short, medium and long-term goals</li>
    <li>Identify roadblocks and disempowering habits</li>
    <li>Create a repeatable process that delivers results</li>
    <li>Transform burned out employees or leaders into fired-up employees</li>
  </ul>
  <div class="callout"><span class="plus-ring">+</span>With over 25 years of experience in a variety of industries, we know the daily attitudes, habits and goals for successful companies begin with a plan. By training employees where needed and coaching to clear expectations writes success stories daily as the plan unfolds over the course of the year.</div>
</section>

<section class="feature">
  <div class="portrait feature-portrait" role="img" aria-label="Portrait photo of Dana Holloway"></div>
  <p class="feature-kicker">Here's to your success!</p>
  <p class="feature-name">Dana Holloway</p>
  <div class="know-more"><span class="plus-ring" style="border-color:#fff;color:#fff">+</span>Know More</div>
</section>

<section class="voices">
  <svg width="34" height="28" viewBox="0 0 34 28">
    <path d="M3 3h18v11H11l-5 5v-5H3z" fill="none" stroke="#e0402a" stroke-width="2.5" stroke-linejoin="round"/>
    <path d="M15 12h16v10h-3v4l-4-4h-9z" fill="none" stroke="#e0402a" stroke-width="2.5" stroke-linejoin="round"/>
  </svg>
  <h2><em>People</em> SAY:</h2>
  <blockquote>"Dana's work proved very valuable in the efforts we undertook to pass on to our 280 employees our Vision, and the Values required in order for us to achieve our Vision. Her involvement was always professional, and appreciated by all of us. Without her contribution we would not have been able to progress to the point where we became independently capable of properly describing and implementing the product of the effort we decided to undertake in 2005."</blockquote>
  <cite><em>Glen Harlow - VP and General Manager of Copper Ridge Mine</em></cite>
</section>

<footer class="contact">
  <p class="signup">Sign up for my <strong>FREE</strong> report "Have Fun While Making Sales" and make more money this month!</p>
  <div class="field field-name">Name</div>
  <div class="field field-email">Email</div>
  <div class="field field-msg">Message<div class="box"></div></div>
  <div class="send">SEND</div>
  <ul class="reach">
    <li>
      <svg width="16" height="18" viewBox="0 0 16 18"><path d="M4 1l3 4-2 2c1 2 3 4 5 5l2-2 4 3-2 3C8 16 1 9 1 4z" fill="#888"/></svg>
      <div><div class="label">Call us</div><div class="value">505 555-0147</div></div>
    </li>
    <li>
      <svg width="16" height="18" viewBox="0 0 16 18"><path d="M8 1a5 5 0 0 1 5 5c0 4-5 11-5 11S3 10 3 6a5 5 0 0 1 5-5z" fill="#888"/><circle cx="8" cy="6" r="2" fill="#1f1f1f"/></svg>
      <div><div class="label">Address</div><div class="value">2280 Mesa Crest NE, #210, Albuquerque, New Mexico, 87110</div></div>
    </li>
    <li>
      <svg width="16" height="18" viewBox="0 0 16 18"><rect x="1" y="4" width="14" height="10" fill="none" stroke="#888" stroke-width="1.6"/><path d="M1 4l7 6 7-6" fill="none" stroke="#888" stroke-width="1.6"/></svg>
      <div><div class="label">Say hello</div><div class="value">hello@brightpath-advisory.net</div></div>
    </li>
  </ul>
</footer>

<footer class="legal">
  <p>©2014 Summit Path Advisory</p>
  <div class="social"><span></span><span></span><span></span><span></span><span></span><span></span></div>
</footer>

</body>
</html>
```